Thank you for shopping with us business card

We would like a thank you card for our rebranded business. We used to be "Brindle Goods" but are now "Marlow Finds. Old thank you card and new logo will be attached for reference. New thank you card does not have to be same design as old thank you card, but please use new logo.
Shopmart URL is now marlowfinds.shopmart.example
Instagram is @Marlow_Finds
Email is marlowfinds@mailbox.example
Thank you!

Contact Information for Business Card

Shopmart site, email, Instagram

```html
<!DOCTYPE html>
<html lang="en">
<head>
<meta charset="utf-8">
<title>Marlow Finds – Thank You Card</title>
<link rel="stylesheet" href="https://fonts.googleapis.com/css2?family=Montserrat:wght@400;500;600;700&family=Arimo:wght@400&family=Allura&display=swap">
<style>
  :root {
    --page: #ffffff;
    --card-light: #5e8ac8;
    --card-dark: #2869b3;
    --ink: #ffffff;
    --shadow: rgba(0, 0, 0, 0.32);
  }
  * { box-sizing: border-box; margin: 0; padding: 0; }
  html, body {
    width: 1200px; height: 1200px; overflow: hidden;
    background: var(--page);
  }
  .card {
    position: absolute;
    left: 196px;
    width: 802px; height: 458px;
    border-radius: 25px;
    background: var(--card-light);
    overflow: hidden;
    box-shadow: 10px 14px 14px var(--shadow);
    color: var(--ink);
  }
  .card--front { top: 91px; }
  .card--back { top: 645px; }
  .card-shape { position: absolute; inset: 0; width: 802px; height: 458px; }
  .brand-mark {
    position: absolute;
    border: 3px solid var(--ink);
    border-radius: 50%;
    width: 84px; height: 84px;
  }
  .brand-name {
    position: absolute;
    width: 300px;
    text-align: center;
    font-family: "Montserrat", sans-serif;
    font-weight: 600;
    font-size: 18px;
    letter-spacing: -0.2px;
    text-transform: uppercase;
  }
  .card--front .brand-mark { left: 359px; top: 70px; }
  .card--front .brand-name { left: 251px; top: 179px; }
  .card--back .brand-mark { left: 88px; top: 163px; }
  .card--back .brand-name { left: -20px; top: 281px; }

  .message {
    position: absolute;
    left: 303px; top: 0;
    width: 460px;
    text-align: center;
  }
  .thanks {
    position: absolute;
    left: 0; top: 28px; width: 460px;
    font-family: "Allura", cursive;
    font-size: 66px;
    line-height: 76px;
    font-weight: 400;
    word-spacing: 18px;
    letter-spacing: 1px;
  }
  .thanks-sub {
    position: absolute;
    left: 0; top: 121px; width: 460px;
    font-family: "Montserrat", sans-serif;
    font-weight: 500;
    font-size: 23px;
    letter-spacing: 5px;
  }
  .note {
    position: absolute;
    left: -10px; top: 176px; width: 480px;
    font-family: "Arimo", sans-serif;
    font-size: 21px;
    line-height: 32px;
    letter-spacing: 1.2px;
  }
  .find-us {
    position: absolute;
    left: 0; top: 290px; width: 460px;
    font-family: "Montserrat", sans-serif;
    font-weight: 700;
    font-size: 21px;
    letter-spacing: 2px;
  }
  .contacts {
    position: absolute;
    left: 355px; top: 326px;
    list-style: none;
    font-family: "Arimo", sans-serif;
    font-size: 21px;
    letter-spacing: 1.1px;
  }
  .contact {
    display: flex; align-items: center;
    height: 31px;
  }
  .contact-icon {
    width: 26px; height: 26px;
    margin-right: 12px;
    flex: none;
  }
</style>
</head>
<body>

<section class="card card--front" aria-label="Card front">
  <svg class="card-shape" viewBox="0 0 802 458" aria-hidden="true">
    <path d="M262,-2 V132 A139 139 0 0 0 540 132 V-2 Z" fill="var(--card-dark)" stroke="var(--ink)" stroke-width="3"/>
  </svg>
  <span class="brand-mark" aria-hidden="true"></span>
  <p class="brand-name">Marlow Finds</p>
</section>

<section class="card card--back" aria-label="Card back">
  <svg class="card-shape" viewBox="0 0 802 458" aria-hidden="true">
    <path d="M0,0 H126 V60 A172.5 172.5 0 0 1 126 398 V458 H0 Z" fill="var(--card-dark)"/>
    <path d="M126,0 V60 A172.5 172.5 0 0 1 126 398 V458" fill="none" stroke="var(--ink)" stroke-width="3"/>
  </svg>
  <span class="brand-mark" aria-hidden="true"></span>
  <p class="brand-name">Marlow Finds</p>

  <div class="message">
    <h1 class="thanks">Thank You</h1>
    <p class="thanks-sub">FOR YOUR PURCHASE !</p>
    <p class="note">Your purchase made my day and I<br>hope this package brightens yours.<br>Please come back and leave a review !</p>
    <p class="find-us">FIND US ON :</p>
  </div>

  <ul class="contacts">
    <li class="contact">
      <svg class="contact-icon" viewBox="0 0 26 26" aria-hidden="true"><circle cx="13" cy="13" r="11.5" fill="none" stroke="var(--ink)" stroke-width="1.5"/></svg>
      <span>marlowfinds.shopmart.example</span>
    </li>
    <li class="contact">
      <svg class="contact-icon" viewBox="0 0 26 26" aria-hidden="true"><circle cx="13" cy="13" r="11.5" fill="none" stroke="var(--ink)" stroke-width="1.5"/></svg>
      <span>@Marlow_Finds</span>
    </li>
    <li class="contact">
      <svg class="contact-icon" viewBox="0 0 26 26" aria-hidden="true">
        <circle cx="13" cy="13" r="11.5" fill="none" stroke="var(--ink)" stroke-width="1.5"/>
        <rect x="6.5" y="8.5" width="13" height="9" rx="1" fill="var(--ink)"/>
        <path d="M6.8,9 L13,14 L19.2,9" fill="none" stroke="var(--card-light)" stroke-width="1.3"/>
      </svg>
      <span>marlowfinds@mailbox.example</span>
    </li>
  </ul>
</section>

</body>
</html>
```